KTR MECHANICAL FRONT WINDOWS DESIGN

I have two windows 2320 length, 1870 depth.
I would like a logo on one window, like the logo on sign we had designed with possibly the gears behind like in sign.
Other window would like same colours as logo with details of business.
The background colour I would maybe like the same as sign but if you think something looks better then happy to see design.
Details on other window:
ALL MECHANICAL REPAIRS, SERVICING AND MAJOR OVERHAULS ON LIGHT, HEAVY VEHICLES, DRILL RIGS, COMPRESSORS AND BOOSTERS
CERTIFIED VEHICLE REPAIRER
0493117254
ktrmechanical55@quellmail.com
Maybe just details in some sort of design or have a picture of a 79 SERIES dune strider, Vorn truck or an engine

```html
<!DOCTYPE html>
<html lang="en">
<head>
<meta charset="utf-8">
<title>KTR Mechanical – Window Services</title>
<link href="https://fonts.googleapis.com/css2?family=Catamaran:wght@800;900&display=swap" rel="stylesheet">
<style>
  :root {
    --navy: #040f33;
    --navy-gear: #0a1f55;
    --red: #8c0000;
    --red-deep: #4a0000;
    --black: #000000;
    --sky: #27aae1;
    --white: #ffffff;
    --steel-light: #e8e8e8;
    --steel-dark: #4a4a4a;
  }
  html, body {
    margin: 0;
    padding: 0;
    width: 1200px;
    height: 967px;
    overflow: hidden;
    background: var(--red);
  }
  .window {
    position: relative;
    width: 1200px;
    height: 967px;
    overflow: hidden;
    font-family: "Catamaran", "Arial Black", sans-serif;
    font-weight: 800;
  }
  .window__art {
    position: absolute;
    inset: 0;
  }
  .services {
    position: absolute;
    left: 0;
    top: 0;
    margin: 0;
    padding: 0;
    list-style: none;
  }
  .services__item {
    position: absolute;
    left: 212px;
    height: 60px;
    white-space: nowrap;
    display: flex;
    align-items: center;
  }
  .services__tick {
    width: 56px;
    height: 56px;
    flex: none;
  }
  .services__text {
    position: absolute;
    left: 83px;
    top: -6px;
    font-size: 53px;
    line-height: 1;
    letter-spacing: 0.5px;
    text-transform: uppercase;
  }
  .is-sky { color: var(--sky); }
  .is-white { color: var(--white); }
  .is-sky .services__tick path { fill: var(--white); }
  .is-white .services__tick path { fill: var(--sky); }

  .contact {
    position: absolute;
    left: 203px;
    top: 808px;
  }
  .contact__row {
    position: relative;
    height: 78px;
    display: flex;
    align-items: center;
  }
  .contact__icon {
    width: 54px;
    height: 54px;
    flex: none;
  }
  .contact__text {
    margin-left: 34px;
    color: var(--white);
    font-weight: 900;
    line-height: 1;
    white-space: nowrap;
  }
  .contact__phone { font-size: 56px; letter-spacing: 1px; }
  .contact__email { font-size: 55px; text-transform: none; }
</style>
</head>
<body>
<main class="window">
  <svg class="window__art" width="1200" height="967" viewBox="0 0 1200 967" aria-hidden="true">
    <defs>
      <linearGradient id="frameRed" x1="0" y1="0" x2="1" y2="0">
        <stop offset="0" stop-color="#8c0000"/>
        <stop offset="0.45" stop-color="#4a0000"/>
        <stop offset="1" stop-color="#8c0000"/>
      </linearGradient>
      <linearGradient id="footerBand" x1="0" y1="0" x2="1" y2="0">
        <stop offset="0" stop-color="#8c0000"/>
        <stop offset="0.5" stop-color="#4a0000"/>
        <stop offset="1" stop-color="#000000"/>
      </linearGradient>
      <linearGradient id="steelH" x1="0" y1="0" x2="1" y2="0">
        <stop offset="0" stop-color="#4a4a4a"/>
        <stop offset="1" stop-color="#f0f0f0"/>
      </linearGradient>
      <linearGradient id="steelV" x1="0" y1="0" x2="0" y2="1">
        <stop offset="0" stop-color="#f0f0f0"/>
        <stop offset="1" stop-color="#4a4a4a"/>
      </linearGradient>
      <radialGradient id="gearGlow" cx="0.5" cy="0.5" r="0.5">
        <stop offset="0" stop-color="#0a1f55" stop-opacity="0.8"/>
        <stop offset="1" stop-color="#0a1f55" stop-opacity="0"/>
      </radialGradient>
    </defs>

    <rect class="frame" width="1200" height="967" fill="url(#frameRed)"/>
    <rect class="footer-band" x="0" y="810" width="1200" height="157" fill="url(#footerBand)"/>

    <path class="panel" fill="#040f33" stroke="#5a0000" stroke-width="3"
      d="M52,8 L600,8 C700,10 720,50 800,52 L1192,52 L1192,230
         C1192,500 1148,600 1148,810 L740,810 C640,806 620,766 520,766
         L9,766 L9,460 C9,300 52,200 52,110 Z"/>

    <g role="img" aria-label="Faint interlocking gears in the background">
      <ellipse cx="940" cy="350" rx="270" ry="270" fill="url(#gearGlow)"/>
      <ellipse cx="275" cy="595" rx="170" ry="170" fill="url(#gearGlow)"/>
      <ellipse cx="750" cy="520" rx="150" ry="150" fill="url(#gearGlow)"/>
      <ellipse cx="960" cy="645" rx="120" ry="120" fill="url(#gearGlow)"/>
      <ellipse cx="560" cy="610" rx="120" ry="120" fill="url(#gearGlow)"/>
    </g>

    <rect role="img" aria-label="Spanner along the top edge" x="228" y="34" width="545" height="16" rx="8" fill="url(#steelH)"/>
    <rect role="img" aria-label="Spanner along the left edge" x="31" y="334" width="20" height="405" rx="8" fill="url(#steelV)"/>
    <rect role="img" aria-label="Spanner along the right edge" x="1148" y="230" width="20" height="488" rx="8" fill="url(#steelV)" transform="rotate(180 1158 474)"/>
    <rect role="img" aria-label="Spanner along the bottom edge" x="334" y="769" width="640" height="16" rx="8" fill="url(#steelH)" transform="rotate(180 654 777)"/>
  </svg>

  <ul class="services">
    <li class="services__item is-sky" style="top:120px">
      <svg class="services__tick" viewBox="0 0 56 56"><path d="M0,27 C6,25 12,30 19,36 C26,20 38,6 55,0 L56,5 C42,15 31,32 21,56 C14,45 8,35 0,27 Z"/></svg>
      <span class="services__text">All mechanical repairs</span>
    </li>
    <li class="services__item is-white" style="top:207px">
      <svg class="services__tick" viewBox="0 0 56 56"><path d="M0,27 C6,25 12,30 19,36 C26,20 38,6 55,0 L56,5 C42,15 31,32 21,56 C14,45 8,35 0,27 Z"/></svg>
      <span class="services__text">Servicing and major</span>
    </li>
    <li class="services__item is-sky" style="top:294px">
      <svg class="services__tick" viewBox="0 0 56 56"><path d="M0,27 C6,25 12,30 19,36 C26,20 38,6 55,0 L56,5 C42,15 31,32 21,56 C14,45 8,35 0,27 Z"/></svg>
      <span class="services__text">Overhauls on light</span>
    </li>
    <li class="services__item is-white" style="top:381px">
      <svg class="services__tick" viewBox="0 0 56 56"><path d="M0,27 C6,25 12,30 19,36 C26,20 38,6 55,0 L56,5 C42,15 31,32 21,56 C14,45 8,35 0,27 Z"/></svg>
      <span class="services__text">Heavy vehicles</span>
    </li>
    <li class="services__item is-sky" style="top:467px">
      <svg class="services__tick" viewBox="0 0 56 56"><path d="M0,27 C6,25 12,30 19,36 C26,20 38,6 55,0 L56,5 C42,15 31,32 21,56 C14,45 8,35 0,27 Z"/></svg>
      <span class="services__text">Drill rigs</span>
    </li>
    <li class="services__item is-white" style="top:554px">
      <svg class="services__tick" viewBox="0 0 56 56"><path d="M0,27 C6,25 12,30 19,36 C26,20 38,6 55,0 L56,5 C42,15 31,32 21,56 C14,45 8,35 0,27 Z"/></svg>
      <span class="services__text">Compressors and boosters</span>
    </li>
    <li class="services__item is-sky" style="top:641px">
      <svg class="services__tick" viewBox="0 0 56 56"><path d="M0,27 C6,25 12,30 19,36 C26,20 38,6 55,0 L56,5 C42,15 31,32 21,56 C14,45 8,35 0,27 Z"/></svg>
      <span class="services__text">Certified vehicle repairer</span>
    </li>
  </ul>

  <div class="contact">
    <div class="contact__row">
      <svg class="contact__icon" viewBox="0 0 54 54" aria-hidden="true">
        <circle cx="27" cy="27" r="27" fill="#27aae1"/>
        <path d="M17,13 C19,12 21,13 22,15 L24,20 C25,22 24,23 22,24 C23,28 26,31 30,33 C31,31 32,30 34,31 L39,34 C41,35 41,37 40,39 C38,42 35,43 32,42 C23,39 16,32 13,23 C12,19 14,15 17,13 Z" fill="#ffffff"/>
        <path d="M29,12 A13,13 0 0 1 42,25" stroke="#ffffff" stroke-width="2.5" fill="none" stroke-linecap="round"/>
        <path d="M29,17 A8,8 0 0 1 37,25" stroke="#ffffff" stroke-width="2.5" fill="none" stroke-linecap="round"/>
      </svg>
      <span class="contact__text contact__phone">0493117254</span>
    </div>
    <div class="contact__row">
      <svg class="contact__icon" viewBox="0 0 54 54" aria-hidden="true">
        <circle cx="27" cy="27" r="27" fill="#27aae1"/>
        <rect x="11" y="17" width="32" height="21" fill="none" stroke="#ffffff" stroke-width="2.5"/>
        <path d="M11,17 L27,30 L43,17 M11,38 L22,26 M43,38 L32,26" fill="none" stroke="#ffffff" stroke-width="2.5"/>
      </svg>
      <span class="contact__text contact__email">ktrmechanical55@quellmail.com</span>
    </div>
  </div>
</main>
</body>
</html>
```